CloudRiver Business Card

I need something that flows with the logo and looks professional but creative. I included the thumbnail file of the photo but will upload the source file once I have it. Colors of business card should flow. I am interested in doing the translucent clear plastic cards as well. My company is called CloudRiver in one word and the contact details are below:

Dale Hollings
555-318-4720
www.CloudRiverTx.example
dhollings_47@mailbox.example
Updates

Too much red. I'd rather focus on the blue and put some silver or grey in there.

New Files uploaded. Like the designs so far and am looking forward to seeing more.

Looking for a whole new direction. Let's forget about the plastic card. Let's focus on the blue more than red. I still haven't seen something that really grabs me.

Industry/Entity Type

Plastic

```html
<!DOCTYPE html>
<html lang="en">
<head>
<meta charset="utf-8">
<title>CloudRiver Business Card</title>
<link href="https://fonts.googleapis.com/css2?family=Lato:wght@400;700;900&display=swap" rel="stylesheet">
<style>
  :root {
    --page-bg: #e8e5e0;
    --card-bg: #1c1c1e;
    --card-edge: #2a2a2d;
    --brand-blue: #1a7fb8;
    --accent-red: #e0262e;
    --silver: #c9c9cc;
    --grey-soft: #9a9a9e;
  }
  * { margin: 0; padding: 0; box-sizing: border-box; }
  html, body {
    width: 1200px;
    height: 1000px;
    overflow: hidden;
    background: var(--page-bg);
    font-family: "Lato", Arial, sans-serif;
  }
  .canvas {
    position: relative;
    width: 1200px;
    height: 1000px;
  }
  .card {
    position: absolute;
    left: 250px;
    width: 700px;
    height: 400px;
    border-radius: 18px;
    background: linear-gradient(160deg, var(--card-edge) 0%, var(--card-bg) 55%);
    box-shadow: 0 6px 18px rgba(0, 0, 0, 0.25);
    overflow: hidden;
  }
  .card--front { top: 70px; }
  .card--back { top: 530px; }

  /* Front */
  .front-brand {
    position: absolute;
    top: 130px;
    left: 0;
    width: 100%;
    text-align: center;
    font-weight: 900;
    font-size: 96px;
    letter-spacing: -1px;
    color: var(--brand-blue);
  }
  .front-url {
    position: absolute;
    top: 262px;
    left: 0;
    width: 100%;
    text-align: center;
    font-weight: 700;
    font-size: 24px;
    color: var(--silver);
  }

  /* Back */
  .holder-name {
    position: absolute;
    top: 42px;
    left: 40px;
    font-weight: 700;
    font-size: 32px;
    color: var(--silver);
    letter-spacing: 0.5px;
  }
  .back-brand {
    position: absolute;
    top: 30px;
    right: 40px;
    font-weight: 900;
    font-size: 50px;
    color: var(--brand-blue);
  }
  .contact-list {
    position: absolute;
    right: 36px;
    bottom: 44px;
    list-style: none;
    text-align: right;
  }
  .contact-item {
    display: flex;
    justify-content: flex-end;
    align-items: center;
    gap: 12px;
    font-size: 21px;
    line-height: 34px;
    color: var(--brand-blue);
  }
  .contact-icon {
    width: 20px;
    height: 20px;
    flex: none;
  }
</style>
</head>
<body>
<main class="canvas">

  <section class="card card--front" aria-label="Business card front">
    <div class="front-brand">CloudRiver</div>
    <div class="front-url">www.CloudRiverTx.example</div>
  </section>

  <section class="card card--back" aria-label="Business card back">
    <div class="holder-name">Dale Hollings</div>
    <div class="back-brand">CloudRiver</div>
    <ul class="contact-list">
      <li class="contact-item">
        <span>555-318-4720</span>
        <svg class="contact-icon" viewBox="0 0 20 20" aria-hidden="true">
          <path d="M5 2.5 L8 2.5 L9 6.5 L7 8 Q9 12 12 13 L13.5 11 L17.5 12 L17.5 15 Q17 17.5 14.5 17.5 Q4 16 2.5 5.5 Q2.5 3 5 2.5 Z" fill="var(--accent-red)"/>
        </svg>
      </li>
      <li class="contact-item">
        <span>dhollings_47@mailbox.example</span>
        <svg class="contact-icon" viewBox="0 0 20 20" aria-hidden="true">
          <rect x="2" y="4.5" width="16" height="11" rx="1" fill="var(--accent-red)"/>
          <path d="M2.5 5 L10 11 L17.5 5" fill="none" stroke="var(--card-bg)" stroke-width="1.4"/>
        </svg>
      </li>
      <li class="contact-item">
        <span>www.CloudRiverTx.example</span>
        <svg class="contact-icon" viewBox="0 0 20 20" aria-hidden="true">
          <circle cx="10" cy="10" r="7.5" fill="none" stroke="var(--accent-red)" stroke-width="1.6"/>
          <ellipse cx="10" cy="10" rx="3.2" ry="7.5" fill="none" stroke="var(--accent-red)" stroke-width="1.4"/>
          <line x1="2.5" y1="10" x2="17.5" y2="10" stroke="var(--accent-red)" stroke-width="1.4"/>
        </svg>
      </li>
    </ul>
  </section>

</main>
</body>
</html>
```